Valtrix Energy Information Site Redesign

Re-vamp current site at valtrixenergy.example to include new logo, verbiage updates as needed, redesign, etc. Company overview and additional information on current Valtrix url.

```html
<!DOCTYPE html>
<html lang="en">
<head>
<meta charset="utf-8">
<title>Valtrix Energy</title>
<link rel="stylesheet" href="https://fonts.googleapis.com/css2?family=Roboto:wght@300;400;500;700&display=swap">
<style>
:root{
  --blue:#1a7fd4;
  --orange:#f0901e;
  --dark:#0b0d12;
  --ink:#222;
  --muted:#666;
  --light:#f6f6f6;
  --white:#fff;
  --client:#1d3f8a;
}
*{box-sizing:border-box;margin:0;padding:0}
html,body{width:1200px;height:4072px;overflow:hidden}
body{font-family:"Roboto",Arial,sans-serif;color:var(--ink);background:var(--white);position:relative}
section,header,footer{position:relative;width:1200px}
.btn{position:absolute;background:var(--orange);color:var(--white);font-size:13px;border-radius:3px;text-align:center;font-weight:500}
.section-title{position:absolute;left:0;width:1200px;text-align:center;font-size:32px;font-weight:400}

/* hero */
.hero{height:665px;background:var(--dark)}
.hero-photo{position:absolute;left:0;top:108px;width:1200px;height:557px;background:radial-gradient(ellipse at 62% 80%,#4aa8ff 0%,#1a4f9a 30%,#0a1a3a 65%,#050912 100%)}
.topbar{position:absolute;left:0;top:0;width:1200px;height:108px;background:#000}
.menu{position:absolute;left:122px;top:45px;width:18px}
.menu span{display:block;height:3px;background:var(--white);margin-bottom:4px}
.brand{position:absolute;left:536px;top:38px;color:var(--blue);font-size:22px;font-weight:500;display:flex;align-items:center;gap:6px}
.brand i{width:14px;height:14px;border-radius:50%;background:var(--orange);display:inline-block}
.top-contact{position:absolute;right:120px;top:44px;color:var(--white);font-size:12px;text-align:right;line-height:18px}
.hero h1{position:absolute;left:155px;top:332px;color:var(--white);font-size:32px;font-weight:400}
.hero p{position:absolute;left:157px;top:378px;width:420px;color:var(--white);font-size:13px;line-height:18px}
.hero .btn{left:160px;top:432px;width:140px;height:32px;line-height:32px}

/* about */
.about{height:470px}
.about h2{position:absolute;left:120px;top:100px;font-size:32px;font-weight:400}
.about .copy{position:absolute;left:120px;top:175px;width:460px;font-size:12.5px;color:var(--muted);line-height:17px}
.about .copy p{margin-bottom:12px}
.about .btn{left:120px;top:325px;width:142px;height:32px;line-height:32px}
.about-video{position:absolute;left:624px;top:79px;width:467px;height:309px;background:linear-gradient(180deg,#1d2733 0%,#4a3a3a 60%,#b0783a 100%)}
.play{position:absolute;left:214px;top:134px;width:40px;height:40px}

/* services */
.services{height:426px;background:var(--blue)}
.service{position:absolute;top:81px;width:190px;text-align:center;color:var(--white)}
.service .ph{height:190px;background:linear-gradient(135deg,#2d4d6e,#8aa3bb)}
.service h3{font-size:19px;font-weight:400;line-height:23px;margin-top:24px}

/* testimonials */
.testimonials{height:611px}
.testimonials .section-title{top:62px}
.testimonials .sub{position:absolute;top:112px;width:1200px;text-align:center;font-size:13px;color:var(--muted)}
.t-card{position:absolute;background:var(--light);text-align:center;box-shadow:0 2px 6px rgba(0,0,0,.08)}
.t-card .avatar{width:100px;height:100px;border-radius:50%;background:linear-gradient(180deg,#c9b7a6,#8d7662);margin:30px auto 10px}
.t-card h4{font-size:15px;font-weight:400}
.t-card .role{color:var(--orange);font-size:11px;margin:3px 0 8px}
.t-card p{font-size:12.5px;line-height:17px;color:#444;padding:0 32px}
.t-card .more{font-size:11px;color:#444;margin-top:8px}
.dots{position:absolute;width:1200px;text-align:center}
.dots i{display:inline-block;width:7px;height:7px;border-radius:50%;background:#333;margin:0 4px}
.dots i.on{background:var(--orange)}

/* blogs */
.blogs{height:570px;background:var(--blue)}
.blogs .section-title{top:22px;color:var(--white)}
.arrows{position:absolute;right:86px;top:38px;display:flex;gap:8px}
.arrows span{width:24px;height:24px;border-radius:50%;background:var(--white)}
.arrows span.on{background:var(--orange)}
.post{position:absolute;top:89px;width:321px;height:373px;background:var(--white)}
.post .ph{height:216px;background:linear-gradient(135deg,#1c3d6a,#6fa2d4)}
.post .meta{height:34px;border-bottom:1px solid #ddd;font-size:11px;color:#444;padding:10px 14px;display:flex;justify-content:space-between}
.post h4{font-size:14px;font-weight:500;padding:16px 14px 6px}
.post p{font-size:11.5px;color:#555;padding:0 14px;line-height:16px}
.post .cont{font-size:11.5px;font-weight:500;padding:14px}
.blogs .btn{left:530px;top:510px;width:140px;height:32px;line-height:32px}

/* clients */
.clients{height:557px}
.clients .section-title{top:58px}
.client{position:absolute;width:190px;height:123px;background:var(--light);display:flex;align-items:center;justify-content:center;text-align:center;padding:0 10px;font-size:17px;font-weight:700;color:var(--client)}

/* contact */
.contact{height:442px;background:var(--light)}
.contact h2{position:absolute;top:38px;font-size:30px;font-weight:400}
.field{position:absolute;left:120px;width:458px;background:var(--white);font-size:12px;padding:11px 12px}
.contact .btn{left:120px;top:339px;width:154px;height:33px;line-height:33px}
.map{position:absolute;left:630px;top:116px;width:470px;height:256px;background:linear-gradient(160deg,#d9e6cf,#c6d9b8 60%,#a9cde8)}

/* footer */
.site-footer{height:331px;background:#000;color:var(--white)}
.site-footer .brand{left:81px;top:50px;font-size:21px}
.f-about{position:absolute;left:81px;top:100px;width:260px;font-size:11px;line-height:15px}
.f-read{position:absolute;left:81px;top:193px;font-size:11px}
.f-col{position:absolute;top:70px;font-size:11px;line-height:16px}
.f-col h5{font-size:16px;font-weight:400;margin-bottom:14px}
.f-col ul{list-style:disc;padding-left:16px}
.f-contact div{display:flex;gap:8px;margin-bottom:6px}
.sub-form{width:225px;height:26px;border:1px solid #fff;border-radius:14px;margin-top:12px;position:relative;font-size:10px;padding:6px 12px}
.sub-form span{position:absolute;right:2px;top:2px;background:var(--white);color:#000;border-radius:11px;padding:3px 8px;font-size:10px;line-height:14px}
.socials{display:flex;gap:8px;margin-top:16px}
.socials i{width:22px;height:22px;border-radius:50%;background:var(--blue)}
.f-rule{position:absolute;left:81px;top:277px;width:1038px;height:1px;background:#555}
.f-bottom{position:absolute;top:294px;font-size:11.5px}
</style>
</head>
<body>

<header class="hero">
  <div class="hero-photo" role="img" aria-label="Glowing blue fingerprint with rising data light strands"></div>
  <div class="topbar">
    <div class="menu"><span></span><span></span><span></span></div>
    <div class="brand"><i></i>Valtrix Energy</div>
    <div class="top-contact">800.555.0142 ☎<br>info@valtrixenergy.example ✉</div>
  </div>
  <h1>Welcome to Valtrix Energy</h1>
  <p>provides the technology to efficiently transfer information electronically and access, integrate and manage data</p>
  <div class="btn">Read More</div>
</header>

<section class="about">
  <h2>About us</h2>
  <div class="copy">
    <p>Valtrix Energy Information has been providing electronic exchange solutions for the energy industry for over 20 years.</p>
    <p>Valtrix utilizes proven data integration techniques to provide customers with cost effective methods to efficiently access, transform and distribute their data. Our customer list includes over 95% of the top 500 energy companies.</p>
  </div>
  <div class="btn">Read More</div>
  <div class="about-video" role="img" aria-label="Video still of harbour cranes silhouetted at dusk">
    <svg class="play" viewBox="0 0 40 40"><circle cx="20" cy="20" r="18" fill="none" stroke="#fff" stroke-width="2"/><path d="M16 12 L28 20 L16 28 Z" fill="#fff"/></svg>
  </div>
</section>

<section class="services">
  <div class="service" style="left:81px"><div class="ph" role="img" aria-label="Engineers reviewing data in a server room"></div><h3>Data Management<br>Solutions</h3></div>
  <div class="service" style="left:293px"><div class="ph" role="img" aria-label="Glowing digital globe held in hands"></div><h3>Well Data<br>Exchange</h3></div>
  <div class="service" style="left:505px"><div class="ph" role="img" aria-label="Hands joining colourful puzzle pieces"></div><h3>Partner Data<br>Exchange</h3></div>
  <div class="service" style="left:717px"><div class="ph" role="img" aria-label="Hand holding a smartphone with an app"></div><h3>E-Ticket<br>Exchange</h3></div>
  <div class="service" style="left:929px"><div class="ph" role="img" aria-label="Businessman in a suit at an office"></div><h3>Owner Relations<br>Services</h3></div>
</section>

<section class="testimonials">
  <h2 class="section-title">Testimonials</h2>
  <div class="sub">Lorem Ipsum is simply dummy text of the printing.</div>
  <div class="t-card" style="left:122px;top:187px;width:277px;height:275px">
    <div class="avatar" role="img" aria-label="Client portrait"></div>
    <h4>Clara Menden</h4><div class="role">Creative Director</div>
    <p>Lorem Ipsum is simply dummy text the printing and typesetting in the Ipsum industry.</p>
    <div class="more">Read More... ⊕</div>
  </div>
  <div class="t-card" style="left:426px;top:157px;width:348px;height:337px;background:#f2f2f2">
    <div class="avatar" role="img" aria-label="Client portrait"></div>
    <h4>Rowan Ellis</h4><div class="role">Creative Director</div>
    <p>“ Lorem Ipsum is simply dummy text the printing and typesetting in the Ipsum industry. ”</p>
    <div class="more">Read More... ⊕</div>
  </div>
  <div class="t-card" style="left:801px;top:187px;width:280px;height:275px">
    <div class="avatar" role="img" aria-label="Client portrait"></div>
    <h4>Tobias Hale</h4><div class="role">Creative Director</div>
    <p>Lorem Ipsum is simply dummy text the printing and typesetting in the Ipsum industry.</p>
    <div class="more">Read More... ⊕</div>
  </div>
  <div class="dots" style="top:526px"><i class="on"></i><i></i><i></i></div>
</section>

<section class="blogs">
  <h2 class="section-title">Blogs</h2>
  <div class="arrows"><span></span><span class="on"></span></div>
  <div class="post" style="left:81px"><div class="ph" role="img" aria-label="Businessman touching a digital network interface"></div><div class="meta"><span>▦ Nov 05 , 2018</span><span>💬 20 &nbsp; ♡ 12</span></div><h4>Blog Post Title 01</h4><p>Lorem Ipsum is simply and dummy printing and typesetting.</p><div class="cont">Continue... ⊕</div></div>
  <div class="post" style="left:439px"><div class="ph" role="img" aria-label="Integration concept with business icons"></div><div class="meta"><span>▦ Nov 05 , 2018</span><span>💬 20 &nbsp; ♡ 12</span></div><h4>Blog Post Title 01</h4><p>Lorem Ipsum is simply and dummy printing and typesetting.</p><div class="cont">Continue... ⊕</div></div>
  <div class="post" style="left:798px"><div class="ph" role="img" aria-label="Glass office towers against the sky"></div><div class="meta"><span>▦ Nov 05 , 2018</span><span>💬 20 &nbsp; ♡ 12</span></div><h4>Blog Post Title 01</h4><p>Lorem Ipsum is simply and dummy printing and typesetting.</p><div class="cont">Continue... ⊕</div></div>
  <div class="btn">View More</div>
</section>

<section class="clients">
  <h2 class="section-title">Our Client</h2>
  <div class="client" style="left:81px;top:149px">Quillmark</div>
  <div class="client" style="left:293px;top:149px">Hollowreach Resources</div>
  <div class="client" style="left:505px;top:149px">Brisenthal</div>
  <div class="client" style="left:717px;top:149px">Ovantara</div>
  <div class="client" style="left:929px;top:149px">Valtrix Energy</div>
  <div class="client" style="left:81px;top:293px">Sorrelby</div>
  <div class="client" style="left:293px;top:293px">Tamberlin</div>
  <div class="client" style="left:505px;top:293px">Corvexa</div>
  <div class="client" style="left:717px;top:293px">Fernhollow Basin</div>
  <div class="client" style="left:929px;top:293px">Lumergas</div>
  <div class="dots" style="top:464px"><i class="on"></i><i></i><i></i><i></i></div>
</section>

<section class="contact">
  <h2 style="left:120px">Contact us</h2>
  <h2 style="left:630px">Map</h2>
  <div class="field" style="top:116px;height:41px">Name</div>
  <div class="field" style="top:176px;height:41px">Phone</div>
  <div class="field" style="top:236px;height:76px">Message</div>
  <div class="btn">Send</div>
  <div class="map" role="img" aria-label="Map of the region showing the office location"></div>
</section>

<footer class="site-footer">
  <div class="brand"><i></i>Valtrix Energy</div>
  <p class="f-about">Valtrix provides technology to efficiently transfer information electronically and access, integrate and manage data. Our services allow companies.</p>
  <div class="f-read">Read More.. ⊕</div>
  <div class="f-col" style="left:391px"><h5>Quick Link</h5><ul><li>Home</li><li>About Us</li><li>Our Service</li><li>Testimonials</li><li>Blogs</li><li>Contact Us</li></ul></div>
  <div class="f-col f-contact" style="left:595px"><h5>Quick Contact</h5>
    <div><span>⌖</span><span>Larkfield Ave. Harlow Bay,<br>Westmere<br>TX 70000</span></div>
    <div><span>☎</span><span>800.555.0176<br>800.555.0193</span></div>
    <div><span>✉</span><span>info@valtrixenergy.example</span></div>
  </div>
  <div class="f-col" style="left:890px"><h5>Subscribe</h5><div>Subscribe For Our Newsletter</div>
    <div class="sub-form">Email Address<span>Subscribe</span></div>
    <div class="socials"><i></i><i></i><i></i><i></i></div>
  </div>
  <div class="f-rule"></div>
  <div class="f-bottom" style="left:81px">CopyRight ©2018 Valtrix Energy. All Right Reserve</div>
  <div class="f-bottom" style="right:81px">Privacy Policy - Terms &amp; Conditions</div>
</footer>

</body>
</html>
```